KPT Building And Maintenance

Need a very professional looking double sided Buisiness card with all my details phone number, name, email, license number.

Target Market(s)

construction industry

Industry/Entity Type

building

Contact Information for Business Card

Name Dale Whitcombe. Email Address Info@KPTBuilding.example.au mobile number 0452918730 licence number 871406D. web site

```html
<!DOCTYPE html>
<html lang="en">
<head>
<meta charset="utf-8">
<title>KPT Building And Maintenance – Business Card</title>
<link rel="stylesheet" href="https://fonts.googleapis.com/css2?family=Exo+2:wght@700&family=Open+Sans:wght@400&display=swap">
<style>
  :root {
    --backdrop: #2b2624;
    --card: #000000;
    --accent: #4a9fe6;
    --ink: #ffffff;
    --rule: #4a4a4a;
  }
  * { margin: 0; padding: 0; box-sizing: border-box; }
  html, body {
    width: 1200px;
    height: 842px;
    overflow: hidden;
    background: var(--backdrop);
  }
  .sheet {
    position: relative;
    width: 1200px;
    height: 842px;
    display: flex;
    align-items: center;
    justify-content: center;
    gap: 40px;
  }
  .card {
    position: relative;
    width: 540px;
    height: 309px;
    background: var(--card);
    overflow: hidden;
    box-shadow: 0 10px 30px rgba(0,0,0,0.5);
  }

  /* Contact side */
  .band {
    position: absolute;
    left: 0;
    width: 100%;
    height: 12px;
    background: var(--accent);
  }
  .band--top { top: 10px; }
  .band--bottom { bottom: 18px; }
  .contact {
    position: absolute;
    inset: 0;
    display: flex;
    flex-direction: column;
    align-items: center;
    justify-content: center;
    text-align: center;
    font-family: "Open Sans", sans-serif;
    color: var(--ink);
    padding-top: 4px;
  }
  .contact__name {
    font-family: "Exo 2", sans-serif;
    font-weight: 700;
    font-size: 26px;
    letter-spacing: 1px;
    color: var(--accent);
    text-transform: uppercase;
    line-height: 1.1;
  }
  .contact__rule {
    width: 150px;
    height: 1px;
    background: var(--rule);
    margin: 8px 0 6px;
  }
  .contact__line {
    font-size: 15px;
    line-height: 1.4;
    letter-spacing: 0.5px;
  }
  .contact__licence {
    font-size: 16px;
    letter-spacing: 0.5px;
    margin-top: 6px;
  }
  .contact__licence-label { color: var(--accent); }

  /* Brand side */
  .tab {
    position: absolute;
    width: 34px;
    height: 70px;
    background: var(--accent);
  }
  .tab--right { right: 0; top: 40px; }
  .tab--left { left: 0; top: 175px; }
  .brand {
    position: absolute;
    inset: 0;
    display: flex;
    align-items: center;
    justify-content: center;
    gap: 12px;
    padding-bottom: 20px;
  }
  .brand__mark {
    width: 18px;
    height: 18px;
    background: var(--accent);
  }
  .brand__name {
    font-family: "Exo 2", sans-serif;
    font-weight: 700;
    font-size: 40px;
    letter-spacing: 1px;
    color: var(--ink);
    text-transform: uppercase;
  }
</style>
</head>
<body>
  <main class="sheet">
    <section class="card card--contact" aria-label="Business card, contact side">
      <div class="band band--top"></div>
      <div class="contact">
        <h1 class="contact__name">Dale Whitcombe</h1>
        <div class="contact__rule"></div>
        <p class="contact__line">0452918730</p>
        <p class="contact__line">Info@KPTBuilding.example.au</p>
        <p class="contact__line">www.KPTBuilding.example.au</p>
        <div class="contact__rule"></div>
        <p class="contact__licence"><span class="contact__licence-label">Licence No.</span> 871406D</p>
      </div>
      <div class="band band--bottom"></div>
    </section>

    <section class="card card--brand" aria-label="Business card, brand side">
      <div class="tab tab--right"></div>
      <div class="tab tab--left"></div>
      <div class="brand">
        <span class="brand__mark"></span>
        <span class="brand__name">KPT Building</span>
      </div>
    </section>
  </main>
</body>
</html>
```